Dr. Halvorsen Announcement

I would like to upload 3 photos of my physicians to send an announcement of our newest physician and addition to our medical group (Brightmoor Eye Medical Group). I would like it glossy something to do with ophthalmology or medical (preferably). I would like to indicate his arrival date August 1, 2014 with office telephone number to start booking appointments for him. Please make it eye catchy and colorful.

something like.
Orders of photos below:
Dr. Gordon T. Wexley & Dr. Martin R. Okafor are proud to announce our newest associate, Dr. L. Marcus Holt-Halvorsen, Dr. Halvorsen is a comprehensive ophthalmologist who is trained in Ouloplastics and Reconstructive surgery at Fenwick University. He will be available soon to schedule appointments or consultations. Please feel free to contact us with any questions (555) 314-2267.

Industry/Entity Type

Medical

Requirements
Must have
• Some kind of "EYE" photo or background

```html
<!DOCTYPE html>
<html lang="en">
<head>
<meta charset="utf-8">
<title>Dr. Halvorsen Announcement – Brightmoor Eye Medical Group</title>
<link rel="stylesheet" href="https://fonts.googleapis.com/css2?family=Arimo:wght@400;700&family=Oswald:wght@500;600&family=Bodoni+Moda:wght@800&display=swap">
<style>
  :root {
    --paper: #ffffff;
    --ink: #161616;
    --stripe-navy: #2b3a8f;
    --stripe-sky: #5fb8e6;
    --name-blue: #3d3a8c;
    --name-purple: #7e2e8e;
    --portrait-dark: #2a3530;
    --portrait-mid: #6f7d74;
  }
  * { margin: 0; padding: 0; box-sizing: border-box; }
  html, body { width: 1200px; height: 881px; overflow: hidden; background: var(--paper); }
  .announcement {
    position: relative;
    width: 1200px;
    height: 881px;
    background: var(--paper);
    font-family: "Arimo", Arial, sans-serif;
    color: var(--ink);
    overflow: hidden;
  }
  .header-art { position: absolute; left: 0; top: 0; }
  .brand-mark {
    position: absolute;
    left: 30px;
    top: 36px;
    display: flex;
    align-items: center;
    gap: 8px;
    font-family: "Oswald", sans-serif;
    font-weight: 500;
    font-size: 20px;
    color: var(--stripe-navy);
  }
  .brand-mark .dot {
    width: 40px; height: 40px;
    border-radius: 50%;
    border: 4px solid var(--stripe-navy);
  }
  .brand-name {
    position: absolute;
    right: 55px;
    top: 8px;
    text-align: right;
    font-family: "Oswald", sans-serif;
    font-weight: 600;
    line-height: 1;
  }
  .brand-name .primary {
    display: block;
    font-size: 68px;
    color: var(--paper);
    letter-spacing: 1px;
  }
  .brand-name .secondary {
    display: block;
    font-size: 36px;
    color: #1c1c1c;
    margin-top: -2px;
  }
  .headline {
    position: absolute;
    left: 215px;
    top: 157px;
    font-family: "Bodoni Moda", serif;
    font-weight: 800;
    font-size: 42px;
    line-height: 46px;
    letter-spacing: 35px;
    color: #111;
    white-space: nowrap;
  }
  .eye-backdrop {
    position: absolute;
    left: 400px;
    top: 330px;
    width: 440px;
    height: 540px;
    border-radius: 50%;
    background: radial-gradient(ellipse at 50% 50%, rgba(120,90,60,0.22) 0 12%, rgba(110,160,190,0.22) 13% 30%, rgba(240,200,170,0.2) 31% 55%, rgba(255,255,255,0) 72%);
  }
  .portrait {
    position: absolute;
    background: radial-gradient(ellipse at 40% 35%, var(--portrait-mid), var(--portrait-dark) 85%);
  }
  .portrait-left { left: 105px; top: 225px; width: 189px; height: 265px; }
  .portrait-right { left: 937px; top: 220px; width: 191px; height: 266px; }
  .portrait-new { left: 540px; top: 222px; width: 150px; height: 200px; }
  .arrival {
    position: absolute;
    left: 294px;
    top: 432px;
    width: 643px;
    text-align: center;
    font-size: 27px;
    line-height: 36px;
    font-weight: 700;
    color: var(--name-purple);
  }
  .message {
    position: absolute;
    left: 103px;
    top: 490px;
    font-size: 37px;
    line-height: 53px;
    white-space: nowrap;
  }
  .message .line { display: block; }
  .message .indent { padding-left: 12px; }
  .name { font-weight: 700; color: var(--name-blue); }
  .name-new { font-weight: 700; color: var(--name-purple); }
  .strong { font-weight: 700; }
</style>
</head>
<body>
<main class="announcement">
  <svg class="header-art" width="1200" height="230" viewBox="0 0 1200 230" aria-hidden="true">
    <defs>
      <linearGradient id="bannerGradient" x1="0" y1="0" x2="0" y2="1">
        <stop offset="0" stop-color="#6e2a82"/>
        <stop offset="0.55" stop-color="#8d3a8f"/>
        <stop offset="1" stop-color="#c45aa0"/>
      </linearGradient>
      <radialGradient id="cornerGlow" cx="0.35" cy="0.4" r="0.7">
        <stop offset="0" stop-color="#f0e04a"/>
        <stop offset="0.5" stop-color="#9ccc3c"/>
        <stop offset="1" stop-color="#5aa832"/>
      </radialGradient>
      <linearGradient id="bandGradient" x1="0" y1="0" x2="0" y2="1">
        <stop offset="0" stop-color="#a6d449"/>
        <stop offset="1" stop-color="#7fbf37"/>
      </linearGradient>
    </defs>
    <rect x="0" y="0" width="1200" height="205" fill="url(#cornerGlow)"/>
    <rect x="130" y="0" width="1070" height="152" fill="url(#bannerGradient)"/>
    <rect x="0" y="152" width="1200" height="53" fill="url(#bandGradient)"/>
    <polygon points="0,205 0,230 395,0 360,0" fill="#ffffff"/>
    <polygon points="0,195 0,222 375,0 345,0" fill="var(--stripe-navy)"/>
    <polygon points="40,180 60,180 345,0 325,0" fill="var(--stripe-sky)"/>
    <polygon points="0,224 0,230 400,0 392,0" fill="#d8e8f0"/>
  </svg>

  <div class="brand-mark"><span class="dot"></span>Brightmoor</div>

  <h1 class="brand-name">
    <span class="primary">BRIGHTMOOR EYE</span>
    <span class="secondary">MEDICAL GROUP, INC.</span>
  </h1>

  <h2 class="headline">ANNOUNCEMENT</h2>

  <div class="eye-backdrop" role="img" aria-label="Faint close-up eye photograph as background"></div>

  <div class="portrait portrait-left" role="img" aria-label="Portrait photo of Dr. Gordon T. Wexley"></div>
  <div class="portrait portrait-new" role="img" aria-label="Portrait photo of Dr. L. Marcus Holt-Halvorsen"></div>
  <div class="portrait portrait-right" role="img" aria-label="Portrait photo of Dr. Martin R. Okafor"></div>

  <p class="arrival">Arriving August 1, 2014</p>

  <p class="message">
    <span class="line"><span class="name">Dr. Gordon T. Wexley</span> &amp; <span class="name">Dr. Martin R. Okafor</span> are proud to</span>
    <span class="line">announce our newest associate, <span class="name-new">Dr. L. Marcus Holt-</span></span>
    <span class="line"><span class="name-new">Halvorsen</span><span class="strong">. Dr. Halvorsen</span> is a comprehensive ophthalmol-</span>
    <span class="line">ogist who is trained in Ouloplastics and Reconstructive</span>
    <span class="line indent">surgery at Fenwick University. He will be available soon to</span>
    <span class="line indent">schedule appointments or consultations. Please feel free</span>
    <span class="line indent">to contact us with any questions&nbsp; <span class="strong">(555) 314-2267</span></span>
  </p>
</main>
</body>
</html>
```